Wellpath Ledgers New Website

Please review the attached Design Brief with additional details. Thank you!

The goal is to create a website that effectively communicates the benefits of WellPath Ledgers to eye care professionals. The website should streamline the process of understanding and utilizing WellPath Ledgers' services, emphasizing improved patient outcomes, increased referrals, and enhanced patient engagement.

Target Market(s)

Eyecare Professionals

Number of Pages Required

4 page

```html
<!DOCTYPE html>
<html lang="en">
<head>
<meta charset="utf-8">
<title>Wellpath Ledgers</title>
<link rel="stylesheet" href="https://fonts.googleapis.com/css2?family=Kumbh+Sans:wght@400;500;600;700&display=swap">
<style>
:root{
  --orange:#ffa53a;
  --blue:#0a5cff;
  --navy:#1b2bb0;
  --navy-dark:#14208f;
  --ink:#111;
  --text:#333;
  --muted:#777;
  --soft:#f4f6fb;
  --line:#dfe3ee;
  --white:#fff;
}
*{box-sizing:border-box;margin:0;padding:0}
html,body{width:1200px;height:5260px;overflow:hidden}
body{font-family:"Kumbh Sans",sans-serif;color:var(--text);background:var(--white);position:relative}
.abs{position:absolute}
.btn{display:inline-flex;align-items:center;justify-content:center;gap:10px;background:var(--navy);color:var(--white);font-weight:700;font-size:12px;border-radius:4px;height:36px;padding:0 40px}
.swoosh{width:52px;height:28px}
.h2{font-size:38px;font-weight:600;color:var(--ink);line-height:1.05}
.p{font-size:13px;line-height:27px;color:var(--text)}

/* top bar */
.topbar{top:0;left:0;width:1200px;height:52px;background:var(--orange);color:var(--white);font-size:11px}
.topbar .item{top:17px;display:flex;align-items:center;gap:14px}
.dot{width:20px;height:20px;border-radius:50%;background:var(--white)}
.soc{width:20px;height:20px;border-radius:50%;background:var(--white);display:inline-block;margin-left:6px}

/* nav */
.logo-card{top:57px;left:135px;width:205px;height:90px;background:var(--white);box-shadow:0 4px 14px rgba(0,0,0,.12);border-radius:4px;display:flex;align-items:center;justify-content:center;gap:8px}
.logo-mark{width:14px;height:14px;border-radius:50%;background:var(--navy)}
.logo-name{font-size:20px;font-weight:600;color:var(--navy)}
.nav{top:86px;left:402px;display:flex;gap:30px;font-size:11px;color:#333}
.nav .on{color:var(--navy);font-weight:700}
.nav-cta{top:75px;left:920px;width:145px;height:38px;padding:0}

/* hero */
.hero-photo{top:128px;left:410px;width:790px;height:544px;background:linear-gradient(120deg,#ffffff 0%,#f1e9e4 30%,#d7b9a3 60%,#8aa0b8 100%)}
.hero-title{top:236px;left:135px;font-size:46px;font-weight:500;line-height:45px;color:var(--ink)}
.hero-title span{color:var(--navy)}
.hero-copy{top:378px;left:135px;width:290px;font-size:14px;line-height:23px}
.hero-btn{top:481px;left:135px;width:151px;padding:0}
.features{top:573px;left:230px;width:740px;height:202px;background:var(--blue);display:flex;padding:30px 33px;color:var(--white)}
.feature{flex:1;padding:0 30px;border-left:1px solid rgba(255,255,255,.5)}
.feature:first-child{border:none}
.feature .ic{width:40px;height:40px;border-radius:50%;background:var(--white);display:flex;align-items:center;justify-content:center}
.feature h3{font-size:14px;font-weight:600;margin:22px 0 12px}
.feature p{font-size:10px;line-height:18px;width:120px}

/* who */
.who-photo{top:888px;left:135px;width:492px;height:537px;border-radius:6px;background:linear-gradient(135deg,#f2f2f2,#e5e0dc 55%,#cfc6c0)}
.who-text{top:900px;left:667px;width:400px}
.bar{margin-top:22px}
.bar .lbl{display:flex;justify-content:space-between;font-size:15px;color:#333;position:relative}
.bar .pct{position:absolute;font-size:13px;color:var(--blue);top:-4px}
.bar .track{height:2px;background:var(--line);margin-top:10px;position:relative}
.bar .fill{height:2px;background:var(--blue);position:relative}
.bar .fill::after{content:"";position:absolute;right:-6px;top:-5px;width:12px;height:12px;border-radius:50%;background:var(--blue)}

/* services */
.services{top:1537px;left:0;width:1200px;height:677px;background:var(--soft)}
.card{position:absolute;top:330px;width:295px;height:237px;background:var(--white);padding:50px 42px 0;box-shadow:0 2px 10px rgba(0,0,0,.04)}
.card .ic{position:absolute;top:-28px;left:42px;width:56px;height:56px;border-radius:6px;background:var(--blue);display:flex;align-items:center;justify-content:center}
.card h3{font-size:17px;font-weight:600;color:var(--ink);margin-top:3px}
.card p{font-size:11px;line-height:20px;margin-top:10px;color:#555}
.card .more{margin-top:12px;font-size:12px;font-weight:700;color:var(--blue);display:flex;align-items:center;gap:10px}
.card.active{background:var(--blue);color:var(--white)}
.card.active h3,.card.active p,.card.active .more{color:var(--white)}
.card.active .ic{background:var(--white)}

/* pricing */
.plan{position:absolute;top:2412px;width:296px;height:533px;background:var(--soft)}
.plan .ph{height:196px;background:linear-gradient(135deg,#e9eef5,#c9d2de 60%,#9aa8bb)}
.plan .price{position:absolute;top:170px;left:35px;width:50px;height:48px;background:var(--white);font-size:16px;font-weight:700;color:var(--ink);text-align:center;padding-top:7px;line-height:1}
.plan .price small{display:block;font-size:8px;font-weight:400;color:#555;margin-top:3px}
.plan.featured .price{background:var(--navy);color:var(--white)}
.plan.featured .price small{color:var(--white)}
.plan h3{margin:42px 0 0 35px;font-size:18px;font-weight:600;color:#222}
.plan ul{list-style:none;margin:18px 35px 0;width:156px}
.plan li{font-size:10px;padding:10px 0;border-bottom:1px solid var(--line)}
.plan li:last-child{border:none}
.plan .btn{margin:22px 0 0 35px;width:151px;padding:0;height:36px}
.plan.featured{background:var(--navy);color:var(--white)}
.plan.featured h3{color:var(--white)}
.plan.featured li{border-color:rgba(255,255,255,.3)}
.plan.featured .btn{background:var(--white);color:var(--ink)}

/* contact */
.contact{top:3055px;left:0;width:1200px;height:673px;background:var(--soft)}
.field{position:absolute;background:var(--white);font-size:10px;color:#444;padding:16px 20px;height:44px}
.contact-photo{position:absolute;top:90px;left:612px;width:570px;height:583px;background:linear-gradient(160deg,#f4f6fb 10%,#d9cfc8 45%,#a39387 80%,#e8eaf0 100%)}

/* testimonials */
.quote{position:absolute;font-size:120px;font-weight:700;line-height:1;font-family:Georgia,serif}
.tcard{position:absolute;width:296px;background:var(--white);text-align:center}
.tcard.side{background:#f7f7f9;opacity:.55;height:254px;top:4029px}
.tcard p{font-size:11px;line-height:22px;padding:0 28px;color:#444}
.arrow-c{position:absolute;width:46px;height:46px;border-radius:50%;display:flex;align-items:center;justify-content:center}

/* footer */
.footer{top:4547px;left:0;width:1200px;height:713px;background:var(--navy);color:var(--white)}
.footer h4{font-size:22px;font-weight:600}
.footer .col{position:absolute;top:336px}
.footer .fp{font-size:12px;line-height:26px}
.footer ul{list-style:none;font-size:11px}
.footer li{line-height:25px}
.fsoc{display:inline-block;width:36px;height:36px;border-radius:50%;background:rgba(255,255,255,.35);margin-right:10px}
.fic{display:inline-block;width:30px;height:30px;border-radius:50%;background:var(--white);vertical-align:middle;margin-right:14px;position:relative}
</style>
</head>
<body>

<svg width="0" height="0" style="position:absolute">
  <defs>
    <symbol id="swoosh" viewBox="0 0 52 28"><path d="M2 24 Q22 26 40 8" stroke="#ffa53a" stroke-width="5" fill="none" stroke-linecap="round"/><path d="M34 4 L48 2 L44 16 Z" fill="#ffa53a"/></symbol>
    <symbol id="eye" viewBox="0 0 24 24"><path d="M2 12 Q12 3 22 12 Q12 21 2 12Z" fill="none" stroke="currentColor" stroke-width="2"/><circle cx="12" cy="12" r="3.5" fill="currentColor"/></symbol>
    <symbol id="arrow" viewBox="0 0 36 10"><path d="M0 5H34M29 1L34 5L29 9" stroke="currentColor" stroke-width="1.5" fill="none"/></symbol>
  </defs>
</svg>

<!-- top bar -->
<header class="abs topbar">
  <div class="abs item" style="left:135px;top:16px"><span class="dot"></span>Opening Hours : 08:00AM to 21:00PM</div>
  <div class="abs item" style="left:483px;top:16px"><span class="dot"></span>contact@wellpathledgers.com</div>
  <div class="abs item" style="left:866px;top:16px">Follow Us On: <span><span class="soc"></span><span class="soc"></span><span class="soc"></span><span class="soc"></span></span></div>
</header>

<!-- nav -->
<div class="abs logo-card"><span class="logo-mark"></span><span class="logo-name">Wellpath Ledgers</span></div>
<nav class="abs nav"><span class="on">Home</span><span>About Us</span><span>Services</span><span>Pricing</span><span>Testimonials</span><span>Blogs</span><span>FAQs</span></nav>
<a class="abs btn nav-cta">Contact Us</a>

<!-- hero -->
<div class="abs hero-photo" role="img" aria-label="Smiling patient wearing an optometry trial frame held by a clinician"></div>
<svg class="abs swoosh" style="top:205px;left:135px"><use href="#swoosh"/></svg>
<h1 class="abs hero-title">Transforming<br><span>Eye Care</span><br>Dynamics</h1>
<p class="abs hero-copy">Lorem Ipsum is simply dummy text of the printing and typesetting industry. Lorem Ipsum</p>
<a class="abs btn hero-btn">Read More</a>

<section class="abs features">
  <div class="feature"><div class="ic"><svg width="18" height="18" viewBox="0 0 18 18"><rect x="2" y="3" width="14" height="12" rx="2" fill="none" stroke="#0a5cff" stroke-width="2"/><path d="M2 7H16" stroke="#0a5cff" stroke-width="2"/></svg></div><h3>Modern UI</h3><p>Lorem Ipsum is simply dummy text of the printing</p></div>
  <div class="feature"><div class="ic"><svg width="18" height="18" viewBox="0 0 18 18"><rect x="3" y="8" width="12" height="9" rx="1" fill="#0a5cff"/><path d="M5.5 8V5.5a3.5 3.5 0 0 1 7 0V8" fill="none" stroke="#0a5cff" stroke-width="2"/></svg></div><h3>Secure System</h3><p>Lorem Ipsum is simply dummy text of the printing</p></div>
  <div class="feature"><div class="ic"><svg width="18" height="18" viewBox="0 0 18 18"><circle cx="9" cy="9" r="7" fill="none" stroke="#0a5cff" stroke-width="2"/><path d="M2 9H16M9 2Q13 9 9 16Q5 9 9 2" fill="none" stroke="#0a5cff" stroke-width="1.5"/></svg></div><h3>Web Based</h3><p>Lorem Ipsum is simply dummy text of the printing</p></div>
</section>

<!-- who we are -->
<div class="abs who-photo" role="img" aria-label="Optometrist presenting an eye chart"></div>
<section class="abs who-text">
  <svg class="swoosh"><use href="#swoosh"/></svg>
  <h2 class="h2" style="margin:6px 0 16px">Who We Are</h2>
  <p class="p">Lorem Ipsum is simply dummy text of the printing and typesetting industry. Lorem Ipsum has been the industry's standard dummy text ever since the 1500s, when an unknown printer took a galley of type and scrambled it to make a type specimen book.</p>
  <div class="bar"><div class="lbl">lorem ipsum<span class="pct" style="left:207px">75%</span></div><div class="track"><div class="fill" style="width:225px"></div></div></div>
  <div class="bar" style="margin-top:36px"><div class="lbl">lorem ipsum<span class="pct" style="left:252px">85%</span></div><div class="track"><div class="fill" style="width:267px"></div></div></div>
  <div class="bar" style="margin-top:36px"><div class="lbl">lorem ipsum<span class="pct" style="left:302px">90%</span></div><div class="track"><div class="fill" style="width:317px"></div></div></div>
  <a class="btn" style="margin-top:36px;width:166px;padding:0">Learn More</a>
</section>

<!-- services -->
<section class="abs services">
  <svg class="abs swoosh" style="top:80px;left:135px"><use href="#swoosh"/></svg>
  <h2 class="abs h2" style="top:110px;left:135px">We Gave The<br>Best For You</h2>
  <div class="abs" style="top:120px;left:427px;width:1px;height:50px;background:#bbb"></div>
  <p class="abs p" style="top:108px;left:473px;width:320px">Lorem Ipsum is simply dummy text of the printing and typesetting industry. Lorem Ipsum has been the industry's</p>
  <div class="abs" style="top:120px;left:848px;width:1px;height:50px;background:#bbb"></div>
  <a class="abs btn" style="top:846px;top:846px;top:846px;top:846px;top:846px;top:846px"></a>
  <div class="card active" style="left:135px"><div class="ic" style="color:var(--blue)"><svg width="24" height="24"><use href="#eye"/></svg></div><h3>Eye Care</h3><p>Lorem Ipsum is simply dummy text of the printing and typesetting industry. Lorem Ipsum has been the industry's</p><div class="more">Read More <svg width="36" height="10"><use href="#arrow"/></svg></div></div>
  <div class="card" style="left:451px"><div class="ic" style="color:#fff"><svg width="26" height="26"><use href="#eye"/></svg></div><h3>Retina Repair</h3><p>Lorem Ipsum is simply dummy text of the printing and typesetting industry. Lorem Ipsum has been the industry's</p><div class="more">Read More <svg width="36" height="10"><use href="#arrow"/></svg></div></div>
  <div class="card" style="left:769px"><div class="ic" style="color:#fff"><svg width="26" height="26"><use href="#eye"/></svg></div><h3>Vision Check</h3><p>Lorem Ipsum is simply dummy text of the printing and typesetting industry. Lorem Ipsum has been the industry's</p><div class="more">Read More <svg width="36" height="10"><use href="#arrow"/></svg></div></div>
</section>
<a class="abs btn" style="top:1667px;left:895px;width:172px;padding:0;background:var(--blue)">View All Services</a>

<!-- pricing -->
<svg class="abs swoosh" style="top:2284px;left:574px"><use href="#swoosh"/></svg>
<h2 class="abs h2" style="top:2318px;left:0;width:1200px;text-align:center">Our Best Pricing Plan</h2>
<div class="plan featured" style="left:135px"><div class="ph" role="img" aria-label="Optician fitting glasses on a patient"></div><div class="price">59<sup style="font-size:8px">$</sup><small>Monthly</small></div><h3>Eye Treatment</h3><ul><li>Regular Health Checkups</li><li>Free Equipment Use</li><li>Advance Options</li><li>GB Stage 16</li></ul><a class="btn">Choose Plan</a></div>
<div class="plan" style="left:451px"><div class="ph" role="img" aria-label="Patient looking through a trial frame during an eye exam"></div><div class="price">69<sup style="font-size:8px">$</sup><small>Monthly</small></div><h3>Professional</h3><ul><li>Regular Health Checkups</li><li>Free Equipment Use</li><li>Advance Options</li><li>GB Stage 16</li></ul><a class="btn">Choose Plan</a></div>
<div class="plan" style="left:769px"><div class="ph" role="img" aria-label="Optometrist in a clinic with an eye chart"></div><div class="price">79<sup style="font-size:8px">$</sup><small>Monthly</small></div><h3>Enterprise</h3><ul><li>Regular Health Checkups</li><li>Free Equipment Use</li><li>Advance Options</li><li>GB Stage 16</li></ul><a class="btn">Choose Plan</a></div>

<!-- contact -->
<section class="abs contact">
  <svg class="abs swoosh" style="top:100px;left:135px"><use href="#swoosh"/></svg>
  <div class="field" style="top:200px;left:135px;width:198px">Your Name</div>
  <div class="field" style="top:200px;left:345px;width:203px">Enter Email</div>
  <div class="field" style="top:256px;left:135px;width:198px">Subject</div>
  <div class="field" style="top:256px;left:345px;width:203px">Phone</div>
  <div class="field" style="top:312px;left:135px;width:413px;height:156px">Message</div>
  <a class="abs btn" style="top:523px;left:135px;width:165px;padding:0;background:var(--blue)">Submit Now <svg width="20" height="10" style="color:#fff"><use href="#arrow"/></svg></a>
  <div class="contact-photo" role="img" aria-label="Two eye care professionals, one holding a trial frame"></div>
</section>

<!-- testimonials -->
<svg class="abs swoosh" style="top:3838px;left:574px"><use href="#swoosh"/></svg>
<h2 class="abs h2" style="top:3874px;left:0;width:1200px;text-align:center">Our Testimonials</h2>
<div class="tcard side" style="left:135px"><div class="quote" style="color:#7a8cff;margin-top:0">&#8221;</div><p style="margin-top:-30px">Lorem Ipsum is simply dummy text of the printing and typesetting industry. Lorem Ipsum has been the industry's standard dummy text ever since the</p></div>
<div class="tcard side" style="left:769px"><div class="quote" style="color:#7a8cff">&#8221;</div><p style="margin-top:-30px">Lorem Ipsum is simply dummy text of the printing and typesetting industry. Lorem Ipsum has been the industry's standard dummy text ever since the</p></div>
<div class="tcard" style="left:451px;top:3994px;height:250px;box-shadow:0 4px 20px rgba(0,0,0,.08)"><div class="quote" style="color:var(--blue);margin-top:-10px">&#8221;</div><p style="margin-top:-18px">Lorem Ipsum is simply dummy text of the printing and typesetting industry. Lorem Ipsum has been the industry's standard dummy text ever since the 1500s, when an unknown printer took</p></div>
<svg class="abs" style="top:4244px;left:592px" width="16" height="8"><path d="M0 0H16L8 8Z" fill="#fff"/></svg>
<div class="arrow-c" style="top:4120px;left:65px;background:#c9d1ff"><svg width="14" height="14"><path d="M9 2L4 7L9 12" stroke="#fff" stroke-width="3" fill="none"/></svg></div>
<div class="arrow-c" style="top:4120px;left:1088px;background:var(--blue)"><svg width="14" height="14"><path d="M5 2L10 7L5 12" stroke="#fff" stroke-width="3" fill="none"/></svg></div>
<div class="abs" role="img" aria-label="Portrait of the reviewer" style="top:4296px;left:570px;width:60px;height:60px;border-radius:50%;background:linear-gradient(135deg,#eee,#c9bfb8)"></div>
<div class="abs" style="top:4370px;left:0;width:1200px;text-align:center;font-size:14px;font-weight:700;color:var(--ink)">Marisol Venn</div>
<div class="abs" style="top:4390px;left:0;width:1200px;text-align:center;font-size:11px;color:#555">CEO</div>

<!-- footer -->
<footer class="abs footer">
  <div class="abs" style="top:120px;left:0;width:1200px;display:flex;justify-content:center;align-items:center;gap:18px"><span style="width:34px;height:34px;border-radius:50%;background:var(--white)"></span><span style="font-size:52px;font-weight:500">Wellpath Ledgers</span></div>
  <div class="col" style="left:142px;width:250px"><h4>About Us</h4><p class="fp" style="margin-top:16px">Lorem Ipsum is simply dummy text of the printing and typesetting industry. Lorem Ipsum has been the industry's</p><div style="margin-top:14px"><span class="fsoc"></span><span class="fsoc"></span><span class="fsoc"></span><span class="fsoc"></span></div></div>
  <div class="abs" style="top:336px;left:453px;width:1px;height:200px;background:rgba(255,255,255,.4)"></div>
  <div class="col" style="left:530px"><h4>Quick Links</h4><ul style="margin-top:18px"><li>Home</li><li>About Us</li><li>Services</li><li>Pricing</li><li>Testimonials</li><li>Blogs</li><li>FAQs</li><li>Contact Us</li></ul></div>
  <div class="abs" style="top:336px;left:752px;width:1px;height:200px;background:rgba(255,255,255,.4)"></div>
  <div class="col" style="left:805px;font-size:13px"><h4>Contact Us</h4>
    <div style="margin-top:28px"><span class="fic"></span>555-014-2210</div>
    <div style="margin-top:28px"><span class="fic"></span>info@wellpathledgers.com</div>
    <div style="margin-top:28px;display:flex;align-items:center"><span class="fic"></span><span style="line-height:22px">14 Larchmont Lane,<br>Riverton 4021</span></div>
  </div>
  <div class="abs" style="top:643px;left:135px;width:930px;height:1px;background:rgba(255,255,255,.4)"></div>
  <div class="abs" style="top:672px;left:0;width:1200px;text-align:center;font-size:12px">© Copyright 2023 <b>Wellpath Ledgers</b> . All Rights Reserved</div>
</footer>

</body>
</html>
```